CoverLantern.com website re-design - modern engaging website creation

We have an existing website. Www.CoverLantern.com - the content on the site and our widgets are custom built. But the layout and design of our site we just put there as we built the functionality around it. We want a new, bold, and modern design aimed at getting visitors to run a life insurance quote and ultimately apply. Our demographic is centered around those between the ages of 30-60. So we are looking at a complete site overhaul with better pictures, buttons, and an extremely modern design.

Target Market(s)

30-50 year olds

Industry/Entity Type

Life insurance

Coding

Coded - Design and coding required

Number of Pages Required

5+ page

Font styles to use
Other font styles liked:
• Rubik

Colors
0054AA
0677BA
7BADD7
CADEEF
E8F1F8
00AB8E
00BBA5
67D7C9
C6EFE9
E9F9F6
59FF00
82FF00
B8FF75
E3FFCB
F4FFEA

Requirements
Must have
• Matching color schemes from existing website. We have custom widgets on our site now and those must be . White space is important to make it simple for the user to navigate
Nice to have
• Same content - different more modern design
Should not have
• Colors outside of our current color scheme. Should NOT be too similar to our existing site.

```html
<!DOCTYPE html>
<html lang="en">
<head>
<meta charset="utf-8">
<title>CoverLantern – Term Life Insurance</title>
<link href="https://fonts.googleapis.com/css2?family=Rubik:wght@300;400;500;600&display=swap" rel="stylesheet">
<style>
:root{
  --blue-dark:#0054AA;
  --blue:#0677BA;
  --blue-mid:#7BADD7;
  --blue-pale:#CADEEF;
  --blue-wash:#E8F1F8;
  --green:#86C540;
  --green-dark:#6FAE2C;
  --ink:#1E1E1E;
  --text:#555;
  --footer:#232323;
  --white:#fff;
}
*{box-sizing:border-box;margin:0;padding:0}
html,body{width:1200px;height:4971px;overflow:hidden}
body{font-family:'Rubik',sans-serif;color:var(--ink);background:var(--white);position:relative}
.abs{position:absolute}
.btn{position:absolute;display:flex;align-items:center;justify-content:center;background:var(--green);color:var(--white);font-weight:500;font-size:16px;border-radius:30px;text-transform:uppercase;letter-spacing:.2px}
.brand{font-weight:400;color:var(--blue)}
.brand span{color:var(--green)}
h2.title{position:absolute;font-weight:500;font-size:40px;color:var(--ink);white-space:nowrap}
.ticks{position:absolute;list-style:none}
.ticks li{position:relative;padding-left:24px;font-size:14.5px;line-height:28px;color:var(--text)}
.ticks li::before{content:"";position:absolute;left:0;top:7px;width:14px;height:14px;border-radius:50%;background:var(--blue)}
.ticks li::after{content:"";position:absolute;left:4.5px;top:10px;width:3px;height:6px;border:solid var(--white);border-width:0 2px 2px 0;transform:rotate(45deg)}
.ticks.light li{color:var(--white)}
.ticks.light li::before{background:var(--white)}
.ticks.light li::after{border-color:var(--blue)}
.ticks.big li{font-size:21px;color:var(--white);padding-left:32px;line-height:44px}
.ticks.big li::before{width:19px;height:19px;top:12px;background:var(--white)}
.ticks.big li::after{left:6.5px;top:16px;width:4px;height:8px;border-color:#6b8aa0}

/* header */
.header{position:absolute;top:0;left:0;width:1200px;height:122px}
.logo{position:absolute;left:110px;top:32px;font-size:54px;letter-spacing:-1px}
.pill{position:absolute;top:14px;height:46px;border:2px solid var(--green);border-radius:24px;color:var(--green);font-weight:500;font-size:15px;display:flex;align-items:center;justify-content:center}
.nav{position:absolute;top:80px;right:112px;display:flex;gap:31px;font-size:17px;color:var(--ink)}

/* hero */
.hero-banner{position:absolute;top:122px;left:0;width:1200px;height:648px;background:linear-gradient(180deg,#6f9fc2 0%,#9dbbd0 45%,#7f9a5a 75%,#546e33 100%)}
.hero-banner h1{position:absolute;left:110px;top:140px;font-size:54px;font-weight:500;color:var(--white)}

/* welcome */
.welcome h2{position:absolute;top:838px;left:0;width:1200px;text-align:center;font-size:40px;font-weight:500}
.welcome .lead{position:absolute;top:906px;left:0;width:1200px;text-align:center;font-size:21px;font-weight:500;color:var(--blue)}
.welcome p{position:absolute;top:952px;left:200px;width:800px;text-align:center;font-size:14.5px;line-height:29px;color:var(--text)}

/* carriers band */
.band{position:absolute;left:0;width:1200px}
.band.pale{background:var(--blue-wash)}
.carriers{top:1242px;height:563px;clip-path:polygon(0 0,1020px 0,1200px 115px,1200px 100%,130px 100%,0 440px)}
.bubble{position:absolute;width:152px;height:152px;border-radius:50%;background:var(--white);display:flex;align-items:center;justify-content:center;font-size:19px;font-weight:500;color:var(--ink)}
.bubble i{display:inline-block;width:14px;height:14px;border-radius:50%;margin-right:6px}
.cluster-name{position:absolute;left:262px;top:1497px;font-size:30px}

/* compare */
.card{position:absolute;top:1888px;width:192px;height:322px;border:1.5px solid #bbb;border-radius:8px;background:var(--white);overflow:hidden;text-align:center}
.card .name{height:97px;display:flex;align-items:center;justify-content:center;font-size:22px;font-weight:500}
.card .price{height:53px;display:flex;align-items:center;justify-content:center;color:var(--white);font-size:27px;font-weight:600}
.card .price sup{font-size:13px;margin-top:-10px}
.card .price small{font-size:13px;font-weight:400;align-self:flex-end;margin-bottom:14px}
.card p{font-size:15px;line-height:23px;color:var(--text);margin-top:22px}

/* virtual agent */
.agent{top:2390px;height:510px;background:linear-gradient(135deg,#2f86c7 0%,var(--blue) 50%,var(--blue-dark) 100%);clip-path:polygon(0 0,1020px 0,1200px 110px,1200px 100%,260px 100%,0 350px)}

/* footer */
.footer{position:absolute;top:4446px;left:0;width:1200px;height:525px;background:var(--footer);clip-path:polygon(0 0,1030px 0,1200px 112px,1200px 100%,0 100%)}
.cta{position:absolute;left:172px;top:4397px;width:856px;height:120px;background:var(--green);border-radius:4px}
.footer-col h4{font-size:17px;font-weight:500;color:var(--white);margin-bottom:12px}
.footer-col p{font-size:14.5px;line-height:34px;color:#ddd}
.social{position:absolute;top:4895px;width:42px;height:42px;border:2px solid var(--green);border-radius:50%}
.featured-box{position:absolute;top:4228px;width:182px;height:90px;border:1.5px solid #ccc;border-radius:4px;display:flex;align-items:center;justify-content:center;font-size:22px;font-weight:500;color:#8a8a8a}
</style>
</head>
<body>

<header class="header">
  <div class="logo brand">Cover<span>Lantern</span></div>
  <div class="pill" style="left:712px;width:222px">CONTINUE APPLICATION</div>
  <div class="pill" style="left:952px;width:136px">CLIENT LOGIN</div>
  <nav class="nav"><span>Free Quote</span><span>No Exam</span><span>Articles</span><span>FAQ's</span><span>About</span><span>Contact</span></nav>
</header>

<section class="hero-banner" role="img" aria-label="Photo of a smiling older man flying a red kite in a grassy meadow with a woman in the background">
  <h1>Term Life Insurance</h1>
  <ul class="ticks big" style="left:110px;top:222px">
    <li>Purchase Life Insurance Online</li>
    <li>Quote Yourself</li>
    <li>Apply in Minutes</li>
  </ul>
  <div class="btn" style="left:112px;top:385px;width:246px;height:62px;font-size:17px">Get Your Quote Now</div>
</section>

<section class="welcome">
  <h2>Welcome to CoverLantern</h2>
  <div class="lead">CoverLantern brings you the first do-it-yourself Life Insurance Platform</div>
  <p>Finally an online experienced designed for you to purchase life insurance your way. We've eliminated pushy life insurance agents and we provide you with a simple online experience designed to help you calculate your Life Insurance needs and pick the policy that best suits your needs. At CoverLantern, you can run your own Life Insurance Quotes, pick your own policy, and apply online in minutes.</p>
  <div class="btn" style="left:522px;top:1100px;width:156px;height:52px">Read More</div>
</section>

<section class="band pale carriers"></section>
<div class="bubble" style="left:261px;top:1280px"><i style="background:var(--green)"></i>Brightway</div>
<div class="bubble" style="left:110px;top:1360px"><i style="background:#c0282d"></i>Northfield</div>
<div class="bubble" style="left:413px;top:1360px"><i style="background:var(--blue-dark)"></i>Plainsview</div>
<div class="bubble" style="left:110px;top:1530px">Harborline</div>
<div class="bubble" style="left:413px;top:1530px"><i style="background:var(--blue)"></i>Keystone</div>
<div class="bubble" style="left:261px;top:1610px"><i style="background:var(--blue)"></i>Shieldmark</div>
<div class="cluster-name brand">Cover<span>Lantern</span></div>
<h2 class="title" style="left:667px;top:1425px">Life Insurance Online</h2>
<p class="abs" style="left:670px;top:1498px;font-size:14.5px;line-height:28px;color:var(--text)">Compare quotes from America's top insurance carriers<br>Pick your policy and apply in minutes</p>
<div class="btn" style="left:672px;top:1588px;width:200px;height:48px">Get Your Quote</div>

<h2 class="title" style="left:110px;top:1870px">Compare &amp; Save</h2>
<ul class="ticks" style="left:112px;top:1942px;width:300px">
  <li style="margin-bottom:28px">Get Quotes without having to enter your contact information.</li>
  <li style="margin-bottom:28px">Decide what's best for you without having to deal with pushy insurance agents.</li>
  <li>Virtual agent tools are available to help you choose what life insurance policy is best for you and your family.</li>
</ul>
<div class="btn" style="left:112px;top:2262px;width:230px;height:50px">Compare Carriers</div>

<div class="card" style="left:478px">
  <div class="name">Northfield</div>
  <div class="price" style="background:var(--blue)">$18.<sup>08</sup><small>/MO</small></div>
  <p>$2,000,000<br>Death Benefit</p><p>20 Year<br>Level Term</p>
</div>
<div class="card" style="left:688px">
  <div class="name">Shieldmark</div>
  <div class="price" style="background:var(--green)">$21.<sup>17</sup><small>/MO</small></div>
  <p>$2,000,000<br>Death Benefit</p><p>20 Year<br>Level Term</p>
</div>
<div class="card" style="left:898px">
  <div class="name" style="color:var(--blue)">Keystone</div>
  <div class="price" style="background:var(--blue)">$23.<sup>28</sup><small>/MO</small></div>
  <p>$2,000,000<br>Death Benefit</p><p>20 Year<br>Level Term</p>
</div>

<section class="band agent"></section>
<div class="abs" role="img" aria-label="Illustration of a friendly blue robot virtual agent holding a clipboard" style="left:236px;top:2410px;width:304px;height:486px;border-radius:40px;background:radial-gradient(circle at 50% 45%,#3a6fd0 0%,#2a5fbf 50%,rgba(42,95,191,0) 72%)"></div>
<h2 class="title" style="left:680px;top:2455px;color:var(--white)">Virtual Agent</h2>
<ul class="ticks light" style="left:680px;top:2530px;width:410px">
  <li style="margin-bottom:28px">Our Virtual Agent Lumi can help you calculate how much death benefit you need.</li>
  <li style="margin-bottom:28px">Lumi can help you figure out what type of Life Insurance is right for you and your family.</li>
  <li>Lumi can evaluate your health history and provide you with accurate quotes.</li>
</ul>
<div class="btn" style="left:680px;top:2795px;width:200px;height:50px">Get Your Quote</div>

<h2 class="title" style="left:110px;top:3005px">Live Agent Support</h2>
<ul class="ticks" style="left:112px;top:3080px;width:380px">
  <li>If you need a Live Agent, CoverLantern has you covered. Our CoverLantern Agents are not paid a commission. So if you have questions our agents have the answers that best suit your needs.</li>
</ul>
<div class="abs" style="left:112px;top:3250px;font-size:14.5px;color:var(--text);display:flex;align-items:center;gap:10px">
  <svg width="14" height="14" viewBox="0 0 24 24"><path fill="#0677BA" d="M6.6 10.8a15.1 15.1 0 006.6 6.6l2.2-2.2a1 1 0 011-.25 11.4 11.4 0 003.6.57 1 1 0 011 1V20a1 1 0 01-1 1A17 17 0 013 4a1 1 0 011-1h3.5a1 1 0 011 1c0 1.25.2 2.45.57 3.6a1 1 0 01-.25 1z"/></svg>
  Call Toll Free: (888) 555-0142</div>
<div class="abs" style="left:112px;top:3307px;font-size:14.5px;color:var(--text);display:flex;align-items:center;gap:10px">
  <svg width="15" height="12" viewBox="0 0 24 18"><rect width="24" height="18" rx="2" fill="#0677BA"/><path d="M1 2l11 8 11-8" stroke="#fff" stroke-width="2" fill="none"/></svg>
  Email: info@coverlantern.com</div>
<div class="btn" style="left:112px;top:3372px;width:230px;height:50px">Compare Carriers</div>
<div class="abs" role="img" aria-label="Photo of a smiling customer support agent wearing a headset" style="left:597px;top:3004px;width:491px;height:416px;background:linear-gradient(120deg,#d9d4cf 0%,#b9a89a 45%,#7a3a3a 100%)"></div>

<section class="band pale" style="top:3515px;height:562px;clip-path:polygon(0 0,1020px 0,1200px 115px,1200px 100%,0 100%,0 100%)"></section>
<div class="abs" role="img" aria-label="Photo of a smiling couple applying for insurance on a laptop" style="left:183px;top:3515px;width:462px;height:562px;background:linear-gradient(135deg,#cfd6dc 0%,#a8b4bf 50%,#6f6a68 100%)"></div>
<h2 class="title" style="left:740px;top:3640px">Apply Online</h2>
<ul class="ticks" style="left:740px;top:3717px;width:350px">
  <li style="margin-bottom:28px">Pick your policy and apply online in minutes.</li>
  <li style="margin-bottom:28px">Secure Online Portal keeps your information safe and secure.</li>
  <li>24/7 access to your policy documents.</li>
</ul>
<div class="btn" style="left:740px;top:3915px;width:200px;height:50px">Get Your Quote</div>

<h2 class="abs" style="top:4140px;left:0;width:1200px;text-align:center;font-size:40px;font-weight:500">Featured</h2>
<svg class="abs" style="left:60px;top:4260px" width="16" height="26" viewBox="0 0 16 26"><path d="M13 2L3 13l10 11" stroke="#666" stroke-width="2.5" fill="none"/></svg>
<svg class="abs" style="left:1116px;top:4260px" width="16" height="26" viewBox="0 0 16 26"><path d="M3 2l10 11-10 11" stroke="#666" stroke-width="2.5" fill="none"/></svg>
<div class="featured-box" style="left:110px">Northfield</div>
<div class="featured-box" style="left:309px">Plainsview</div>
<div class="featured-box" style="left:508px">Crestline</div>
<div class="featured-box" style="left:707px">Shieldmark</div>
<div class="featured-box" style="left:906px">Keystone</div>

<footer class="footer"></footer>
<div class="cta">
  <div class="abs" style="left:60px;top:37px;font-size:36px;font-weight:500;color:var(--white)">Compare Quotes</div>
  <div class="abs" style="left:580px;top:34px;width:200px;height:52px;border-radius:28px;background:var(--white);color:var(--ink);font-size:15px;font-weight:500;display:flex;align-items:center;justify-content:center">GET YOUR QUOTE</div>
</div>
<div class="abs" style="left:110px;top:4592px;font-size:56px;color:var(--white);letter-spacing:-1px">CoverLantern</div>
<div class="abs footer-col" style="left:508px;top:4588px">
  <h4>Products</h4>
  <p>10 Year Level Team<br>15 Year Level Team<br>20 Year Level Team<br>30 Year Level Team<br>Lifetime Coverage</p>
</div>
<div class="abs footer-col" style="left:723px;top:4588px;width:300px">
  <h4>Contact</h4>
  <p style="line-height:23px;padding-left:22px;position:relative"><svg style="position:absolute;left:0;top:4px" width="11" height="15" viewBox="0 0 12 16"><path fill="#86C540" d="M6 0a6 6 0 00-6 6c0 4.5 6 10 6 10s6-5.5 6-10a6 6 0 00-6-6zm0 8.5A2.5 2.5 0 116 3.5a2.5 2.5 0 010 5z"/></svg>4820 meadow lake drive, suite 210<br>orlando, fl 32801</p>
  <p style="line-height:23px;padding-left:22px;margin-top:12px;position:relative"><svg style="position:absolute;left:0;top:6px" width="13" height="10" viewBox="0 0 24 18"><rect width="24" height="18" rx="2" fill="#86C540"/><path d="M1 2l11 8 11-8" stroke="#232323" stroke-width="2" fill="none"/></svg>info@coverlantern.com</p>
  <p style="line-height:23px;padding-left:22px;margin-top:20px;position:relative"><svg style="position:absolute;left:0;top:4px" width="12" height="12" viewBox="0 0 24 24"><path fill="#86C540" d="M6.6 10.8a15.1 15.1 0 006.6 6.6l2.2-2.2a1 1 0 011-.25 11.4 11.4 0 003.6.57 1 1 0 011 1V20a1 1 0 01-1 1A17 17 0 013 4a1 1 0 011-1h3.5a1 1 0 011 1c0 1.25.2 2.45.57 3.6a1 1 0 01-.25 1z"/></svg>1-888-555-0187</p>
  <p style="line-height:23px;padding-left:22px;margin-top:20px;position:relative"><svg style="position:absolute;left:0;top:4px" width="13" height="13" viewBox="0 0 24 24"><circle cx="12" cy="12" r="10" stroke="#86C540" stroke-width="2.5" fill="none"/><path d="M12 6v6l4 2" stroke="#86C540" stroke-width="2.5" fill="none"/></svg>Monday – Friday<br>9:00 AM – 8:00 PM</p>
</div>
<div class="abs" role="img" aria-label="Chat button showing the virtual agent mascot" style="left:1093px;top:4753px;width:80px;height:80px;border-radius:50%;background:var(--white);box-shadow:0 2px 8px rgba(0,0,0,.3)"><div style="margin:18px auto;width:34px;height:44px;border-radius:12px;background:var(--blue)"></div></div>
<div class="abs" style="left:110px;top:4894px;width:980px;border-top:1px solid #444"></div>
<div class="abs" style="left:110px;top:4908px;font-size:14.5px;color:#ddd">Copyright © 2022, CoverLantern. All rights reserved.</div>
<div class="social" style="left:830px"></div>
<div class="social" style="left:883px"></div>
<div class="social" style="left:936px"></div>
<div class="social" style="left:989px"></div>
<div class="social" style="left:1042px"></div>

</body>
</html>
```